Website for Excavator and Earthworks Company

We require a modern, sleek and practical website for our newly created earthworks/excavator business in Perth, Western Australia called Kolbane Ridge Earthworks.

The website should have a modern, cutting edge feel but only needs to be relatively simplistic in it's layout and eventual functionality.

Some pages it should have would be Home, About, Projects and Contact Us.

```html
<!DOCTYPE html>
<html lang="en">
<head>
<meta charset="utf-8">
<title>Kolbane Ridge Earthworks</title>
<link href="https://fonts.googleapis.com/css2?family=Poppins:wght@400;500;600;700&display=swap" rel="stylesheet">
<style>
:root{
  --lime:#c8e11c;
  --navy:#0b1829;
  --deep:#0f2a6b;
  --ink:#1d1d1d;
  --muted:#5a5a5a;
  --mint:#f1f8dc;
  --white:#ffffff;
}
*{box-sizing:border-box;margin:0;padding:0}
html,body{width:1200px;height:2788px;overflow:hidden}
body{font-family:'Poppins',sans-serif;color:var(--ink);background:var(--white);position:relative}
a{color:inherit;text-decoration:none}

/* hero */
.hero{position:absolute;left:0;top:0;width:1200px;height:620px;overflow:hidden}
.hero-photo{position:absolute;inset:0;background:linear-gradient(100deg,#1c2a3a 0%,#3a4a55 35%,#8a6a3a 62%,#c98a2a 75%,#52606a 100%)}
.hero-shade{position:absolute;inset:0;background:linear-gradient(90deg,rgba(8,16,30,.75),rgba(8,16,30,.25))}
.brand{position:absolute;left:64px;top:22px;display:flex;align-items:center;gap:12px;color:var(--white);font-weight:700;font-size:20px;line-height:1.1;width:230px}
.brand-mark{width:38px;height:38px;background:var(--lime);flex:none}
.nav{position:absolute;left:432px;top:66px;display:flex;gap:42px;color:var(--white);font-size:18px;font-weight:500}
.pills{position:absolute;right:76px;top:18px;display:flex;gap:16px}
.pill{background:var(--white);color:var(--ink);border-radius:20px;padding:6px 18px;font-size:15px;display:flex;align-items:center;gap:8px}
.pill.phone{background:var(--lime)}
.hero-copy{position:absolute;left:300px;top:170px;width:620px;color:var(--white)}
.hero-copy h1{font-size:62px;font-weight:700;line-height:1.1}
.hero-copy h1 span{color:var(--lime);font-weight:500}
.hero-copy p{font-size:17px;line-height:1.45;margin-top:12px}
.hero-btns{display:flex;gap:22px;margin-top:26px}
.btn{display:inline-block;padding:12px 30px;font-size:17px;font-weight:500;color:var(--white);border:2px solid var(--white)}
.btn.solid{background:var(--deep);border-color:var(--deep)}
.hero-edge{position:absolute;left:0;top:440px}

/* about */
.section-title{text-align:center;font-size:42px;font-weight:600}
.about-title{position:absolute;top:658px;width:1200px}
.about-title::after,.projects-head h2::after{content:"";display:block;width:180px;height:2px;background:var(--lime);margin:10px auto 0}
.about-media{position:absolute;left:60px;top:772px;width:532px;height:368px}
.ph{position:absolute;background:linear-gradient(160deg,#8fb3cf,#d1a14a 60%,#7a6a4a)}
.about-text{position:absolute;left:620px;top:832px;width:500px;font-size:16px;line-height:1.5}
.about-text h3{font-size:19px;font-weight:600;margin-bottom:6px}
.about-text p{color:var(--muted)}
.founder{display:inline-block;margin-top:14px;font-weight:600;text-decoration:underline}

/* projects */
.projects{position:absolute;left:0;top:1180px;width:1200px;height:600px;background:var(--mint)}
.projects-head{position:absolute;top:52px;width:1200px;text-align:center}
.projects-head h2{font-size:42px;font-weight:600}
.projects-head h2 span{color:#9cc20f}
.projects-head p{font-size:16px;color:var(--muted);margin-top:10px;line-height:1.5}
.cards{position:absolute;left:140px;top:192px;display:flex;gap:22px}
.card{width:300px;height:392px;background:var(--white);box-shadow:0 4px 14px rgba(0,0,0,.12);padding:16px}
.card .shot{height:176px;background:linear-gradient(160deg,#9ab7c9,#c8963c 60%,#6b5a40)}
.card h3{font-size:20px;font-weight:600;line-height:1.2;margin-top:14px}
.card p{font-size:13px;color:var(--muted);line-height:1.45;margin-top:8px}
.card .more{display:inline-block;background:var(--lime);font-size:13px;font-weight:600;padding:5px 14px;margin-top:12px}

/* contact */
.contact{position:absolute;left:0;top:1820px;width:1200px;height:660px}
.contact-photo{position:absolute;inset:0;background:linear-gradient(120deg,#0f1f30 0%,#1d3a4c 45%,#3b6270 75%,#1a2d3d 100%)}
.contact h2{position:absolute;left:100px;top:80px;font-size:44px;font-weight:600;color:var(--white)}
.contact-form{position:absolute;left:100px;top:160px;width:520px;color:var(--white)}
.contact-form label{display:block;font-size:15px;margin-top:14px}
.field{height:38px;border:1px solid rgba(255,255,255,.6);margin-top:4px;font-size:14px;color:rgba(255,255,255,.6);padding:8px 12px}
.field.big{height:86px}
.submit{display:inline-block;margin-top:28px;background:var(--lime);color:var(--ink);font-weight:600;font-size:18px;padding:10px 32px}

/* footer */
.footer{position:absolute;left:0;top:2520px;width:1200px;height:268px;background:var(--navy);color:var(--white);border-top:4px solid var(--lime)}
.footer .brand{position:static;width:auto;flex-direction:column;align-items:flex-start}
.foot-brand{position:absolute;left:120px;top:50px;font-weight:700;font-size:22px;line-height:1.2;display:flex;flex-direction:column;gap:10px}
.foot-brand .brand-mark{width:42px;height:42px;background:var(--lime)}
.col{position:absolute;top:52px;font-size:16px;line-height:1.9}
.col h4{font-size:20px;font-weight:500;margin-bottom:6px}
.col.links{left:352px}
.col.projects-list{left:608px}
.col.news{left:860px;width:260px}
.signup{display:flex;align-items:center;gap:6px;margin-top:4px}
.signup .inbox{width:190px;height:26px;background:var(--white);color:#888;font-size:12px;padding:3px 8px}
.signup .go{width:26px;height:26px;background:var(--white);display:flex;align-items:center;justify-content:center}
.socials{display:flex;gap:12px;margin-top:16px;padding-left:24px}
.socials span{width:30px;height:30px;background:#2a5a8a}
.copyright{position:absolute;left:0;bottom:0;width:1200px;height:20px;background:var(--lime);color:var(--ink);font-size:11px;text-align:center;line-height:20px}
</style>
</head>
<body>

<header class="hero">
  <div class="hero-photo" role="img" aria-label="Excavator working on a construction site with buildings behind"></div>
  <div class="hero-shade"></div>
  <div class="brand"><span class="brand-mark"></span>Kolbane Ridge Earthworks</div>
  <nav class="nav"><a href="#">Home</a><a href="#">About</a><a href="#">Projects</a><a href="#">Contact Us</a></nav>
  <div class="pills">
    <span class="pill"><svg width="16" height="12" viewBox="0 0 16 12"><rect x="1" y="1" width="14" height="10" fill="none" stroke="#1d1d1d" stroke-width="1.5"/><path d="M1 1l7 6 7-6" fill="none" stroke="#1d1d1d" stroke-width="1.5"/></svg>hello@kolbaneridge.com</span>
    <span class="pill phone"><svg width="14" height="14" viewBox="0 0 24 24"><path d="M6.6 10.8a15 15 0 006.6 6.6l2.2-2.2a1 1 0 011-.25 11.4 11.4 0 003.6.6 1 1 0 011 1V20a1 1 0 01-1 1A17 17 0 013 4a1 1 0 011-1h3.5a1 1 0 011 1 11.4 11.4 0 00.6 3.6 1 1 0 01-.25 1z" fill="#1d1d1d"/></svg>08 5550 1234</span>
  </div>
  <div class="hero-copy">
    <h1>SOLUTIONS <span>for your need</span></h1>
    <p>Lorem ipsum dolor sit amet, consectetur adipiscing elit. Fusce dapibus in consequat felis, facilisi aliquet purus volutpat nunc consectetur dolor elementum quis.</p>
    <div class="hero-btns"><a class="btn solid" href="#">See more</a><a class="btn" href="#">Contact Us</a></div>
  </div>
  <svg class="hero-edge" width="1200" height="180" viewBox="0 0 1200 180">
    <polygon points="0,40 520,150 1200,20 1200,70 520,180 0,80" fill="#c8e11c"/>
    <polygon points="0,80 520,180 1200,70 1200,180 0,180" fill="#ffffff"/>
    <polygon points="0,60 520,166 1200,44 1200,52 520,174 0,68" fill="#ffffff" opacity=".55"/>
  </svg>
</header>

<h2 class="section-title about-title">About Us</h2>
<div class="about-media">
  <div class="ph" style="left:0;top:0;width:228px;height:178px" role="img" aria-label="Excavator beside apartment towers"></div>
  <div class="ph" style="left:0;top:190px;width:228px;height:178px" role="img" aria-label="Excavator digging on site"></div>
  <div class="ph" style="left:240px;top:0;width:292px;height:368px" role="img" aria-label="Excavator arm lifting soil"></div>
</div>
<div class="about-text">
  <h3>History</h3>
  <p>Lorem ipsum dolor sit amet, consectetur adipiscing elit. Sed perferendis? Quod deleniti alias dolores numquam, omnis ut ullam unde nemo officia temporibus quia quo libero neque quisquam recusandae. Alias repudiandae molestiae consectetur, aut illo voluptatibus fugiat? Ea placeat iure dicta et provident, porro nulla, sit eveniet ratione, dolores laudantium.</p>
  <a class="founder" href="#">Company Founder</a>
</div>

<section class="projects">
  <div class="projects-head">
    <h2>Our <span>projects</span></h2>
    <p>Lorem ipsum dolor, sit amet consectetur adipisicing elit.<br>Excepturi, consequuntur.</p>
  </div>
  <div class="cards">
    <article class="card">
      <div class="shot" role="img" aria-label="Excavator dredging an irrigation channel"></div>
      <h3>Irrigation dredging</h3>
      <p>Lorem ipsum dolor sit amet consectetur adipisicing elit. Distinctio vel quo officia velit deserunt quod fugiat voluptatibus similique necessitatibus dolorem ea harum incidunt.</p>
      <a class="more" href="#">Contact Us ›</a>
    </article>
    <article class="card">
      <div class="shot" role="img" aria-label="Excavator levelling agricultural land"></div>
      <h3>Land leveling of agricultural land</h3>
      <p>The process of dredging the layer of soil or unwanted material above the land, deposit is removed first, for the land to be ready for building.</p>
      <a class="more" href="#">Contact Us ›</a>
    </article>
    <article class="card">
      <div class="shot" role="img" aria-label="Excavator digging land for irrigation"></div>
      <h3>Excavation of land for irrigation</h3>
      <p>Excavation work for irrigation is a crucial part of the construction and consolidation of water networks to ensure a smooth distribution flow.</p>
      <a class="more" href="#">Contact Us ›</a>
    </article>
  </div>
</section>

<section class="contact">
  <div class="contact-photo" role="img" aria-label="Blurred city office scene in dark blue tones"></div>
  <h2>Contact Us</h2>
  <form class="contact-form">
    <label>First Name</label><div class="field">Your Name</div>
    <label>Last Name</label><div class="field">Your last name</div>
    <label>e-mail</label><div class="field">Your e-mail</div>
    <label>Mobile</label><div class="field">Your mobile</div>
    <label>Subject</label><div class="field big">Write something</div>
    <span class="submit">Submit</span>
  </form>
</section>

<footer class="footer">
  <div class="foot-brand"><span class="brand-mark"></span>Kolbane Ridge<br>Earthworks</div>
  <div class="col links"><h4>Quick Links</h4>Home<br>About Us<br>Projects<br>Contact Us</div>
  <div class="col projects-list"><h4>Projects</h4>Installation Irrigation<br>Land leveling<br>Excavation of land</div>
  <div class="col news">
    <h4>Newsletter</h4>
    <div class="signup">
      <svg width="18" height="14" viewBox="0 0 16 12"><rect x="1" y="1" width="14" height="10" fill="none" stroke="#fff" stroke-width="1.5"/><path d="M1 1l7 6 7-6" fill="none" stroke="#fff" stroke-width="1.5"/></svg>
      <span class="inbox">Enter your email</span>
      <span class="go"><svg width="12" height="12" viewBox="0 0 12 12"><path d="M2 6h8M7 3l3 3-3 3" stroke="#0b1829" stroke-width="1.6" fill="none"/></svg></span>
    </div>
    <div class="socials"><span></span><span></span><span></span><span></span></div>
  </div>
  <div class="copyright">Copyright © 2020 Kolbane Ridge Earthworks - All Rights Reserved</div>
</footer>

</body>
</html>
```